I need a design for Corvane Homes which is a custom home builder. The name on it will be Dan Hartley, and I will give the phone number to the winning design. No address or website needed.

```html
<!DOCTYPE html>
<html lang="en">
<head>
<meta charset="utf-8">
<title>Corvane Homes – Business Card</title>
<link rel="stylesheet" href="https://fonts.googleapis.com/css2?family=Raleway:wght@200&family=Roboto+Condensed:wght@400&family=Roboto:wght@400;500&display=swap">
<style>
  :root {
    --backdrop: #2b2b2b;
    --card: #ffffff;
    --ink: #1a1a1a;
    --ink-soft: #8c8c8c;
    --brand-red: #d8221a;
    --brand-gold: #d09a1c;
    --brand-brown: #7e4b2c;
    --brand-grey: #b9c1c6;
  }
  html, body {
    margin: 0;
    width: 1200px;
    height: 1000px;
    overflow: hidden;
    background: var(--backdrop);
  }
  .stage {
    width: 1200px;
    height: 1000px;
    display: flex;
    align-items: center;
    justify-content: center;
  }
  .card {
    position: relative;
    width: 460px;
    height: 740px;
    background: var(--card);
    border-radius: 40px;
    overflow: hidden;
  }
  .brand-name {
    position: absolute;
    top: 190px;
    left: 0;
    right: 0;
    display: flex;
    align-items: center;
    justify-content: center;
    gap: 14px;
    font-family: "Raleway", sans-serif;
    font-weight: 200;
    font-size: 54px;
    color: var(--ink);
    letter-spacing: -0.5px;
  }
  .brand-square {
    width: 14px;
    height: 14px;
    background: var(--brand-red);
  }
  .person {
    position: absolute;
    top: 286px;
    right: 44px;
    text-align: right;
  }
  .person-name {
    font-family: "Roboto Condensed", sans-serif;
    font-size: 38px;
    color: var(--ink);
    line-height: 1;
  }
  .person-title {
    font-family: "Roboto", sans-serif;
    font-size: 16px;
    letter-spacing: 3px;
    color: var(--ink-soft);
    margin-top: 4px;
  }
  .contacts {
    position: absolute;
    top: 430px;
    left: 44px;
    margin: 0;
    font-family: "Roboto", sans-serif;
    font-size: 18px;
    color: var(--ink);
    line-height: 1.4;
    display: grid;
    grid-template-columns: 32px auto;
  }
  .contacts dt { font-weight: 500; }
  .contacts dd { margin: 0; }
  .accent-band {
    position: absolute;
    left: 0;
    right: 0;
    bottom: 0;
    height: 230px;
    background: linear-gradient(90deg, var(--brand-red) 0%, var(--brand-gold) 55%, var(--brand-grey) 100%);
  }
</style>
</head>
<body>
  <main class="stage">
    <article class="card">
      <div class="brand-name"><span class="brand-square"></span>Corvane Homes</div>
      <div class="person">
        <div class="person-name">Dan Hartley</div>
        <div class="person-title">CEO</div>
      </div>
      <dl class="contacts">
        <dt>T:</dt><dd>+92 42 7310428</dd>
        <dt>M:</dt><dd>+92 322 4810275</dd>
        <dt>E:</dt><dd>d.hartley@mailbox.com</dd>
      </dl>
      <div class="accent-band" role="img" aria-label="Brand decoration area in red, gold and grey tones"></div>
    </article>
  </main>
</body>
</html>
```